Wollondilly ridge aerial works business card size advertising

I’m after a simple design , please see attached photo . Im after the same color green in the photo as the base color and the the little white man but instead of him holding a spanner i would like him to be holding a tv antenna pointing an angle , see attached photo of the antenna , i would like him on the left of the business card and the business name to fit in on the right with the phone number . ( if the antenna idea looks stupid , leave him holding a spanner ) On the reverse side of the card i would like a white background with green writing stating some of the services we provide which are the following .Antenna installations and repairs Wall mounting of tv’s Additional TV outlets Brolga satellite supply and installations Brindale , Yarrowmere , Tindalup , Kestrel Flat , Marrowgate , Culvera , All rural areas All in all i would like the business card to compliment my invoices as pictured “ invoice supplied is a dummy invoice “

Contact Information for Business Card

wollondilly ridge aerial works 0418563927

Font styles to use
Sans Serif

Colors
9bcb3c

Requirements
Must have
• what i ask for in project description

```html
<!DOCTYPE html>
<html lang="en">
<head>
<meta charset="utf-8">
<title>Wollondilly Ridge Aerial Works – Business Card</title>
<link rel="stylesheet" href="https://fonts.googleapis.com/css2?family=Roboto+Condensed:wght@400;500;700&display=swap">
<style>
  :root {
    --stage: #58585a;
    --card: #ffffff;
    --ink: #454648;
    --green: #6cc07d;
    --faint: #eceded;
  }
  * { margin: 0; padding: 0; box-sizing: border-box; }
  html, body {
    width: 1200px; height: 1161px; overflow: hidden;
    background: var(--stage);
    font-family: "Roboto Condensed", "Arial Narrow", sans-serif;
    color: var(--ink);
  }
  .card {
    position: absolute;
    background: var(--card);
    width: 915px; height: 522px;
    box-shadow: 0 10px 24px rgba(0,0,0,0.35);
    overflow: hidden;
  }
  .card--front { left: 39px; top: 38px; }
  .card--back { left: 244px; top: 599px; }

  /* front */
  .installer-figure {
    position: absolute; left: 38px; top: 72px;
    width: 203px; height: 354px;
    background: var(--green);
  }
  .brand {
    position: absolute; left: 336px; top: 96px; width: 538px;
    text-align: center;
  }
  .brand__name {
    font-weight: 700; font-size: 66px; line-height: 1.08;
    color: var(--ink);
  }
  .brand__name span { display: block; white-space: nowrap; }
  .brand__phone {
    margin-top: 34px;
    font-weight: 700; font-size: 96px; line-height: 1; white-space: nowrap;
  }

  /* back */
  .aerial-decor {
    position: absolute; right: 40px; top: 30px;
    width: 210px; height: 492px;
    background: linear-gradient(180deg, var(--faint), rgba(236,237,237,0));
  }
  .circuit-decor {
    position: absolute; left: 0; bottom: 0;
    width: 250px; height: 210px;
    background: radial-gradient(circle at 0 100%, rgba(236,237,237,0.9), rgba(255,255,255,0) 70%);
  }
  .services { position: absolute; inset: 0; }
  .services__line {
    position: absolute; left: 0; width: 100%;
    text-align: center; font-size: 40px; line-height: 1;
    white-space: nowrap;
  }
  .services__line--lead { font-weight: 700; font-size: 45px; top: 76px; }
  .services__line--1 { top: 145px; }
  .services__line--2 { top: 210px; }
  .services__line--3 { top: 272px; }
  .services__line--4 { top: 335px; }
  .services__line--area { top: 399px; color: var(--green); font-weight: 500; }
</style>
</head>
<body>
  <section class="card card--front">
    <div class="installer-figure" role="img" aria-label="Illustration of a white installer figure in a hard hat holding a TV antenna on a green panel"></div>
    <div class="brand">
      <h1 class="brand__name"><span>WOLLONDILLY RIDGE</span><span>AERIAL WORKS</span></h1>
      <div class="brand__phone">0418 563 927</div>
    </div>
  </section>

  <section class="card card--back">
    <div class="aerial-decor" role="img" aria-label="Faint decorative TV antenna on a mast"></div>
    <div class="circuit-decor" role="img" aria-label="Faint decorative circuit-board pattern"></div>
    <div class="services">
      <p class="services__line services__line--lead">Antenna installations and repairs</p>
      <p class="services__line services__line--1">Wall mounting of tv’s</p>
      <p class="services__line services__line--2">Additional TV outlets Brolga satellite supply</p>
      <p class="services__line services__line--3">and installations Brindale , Yarrowmere ,</p>
      <p class="services__line services__line--4">Tindalup , Kestrel Flat , Marrowgate , Culvera</p>
      <p class="services__line services__line--area">All rural areas All in all</p>
    </div>
  </section>
</body>
</html>
```